Marrow Business Cards

Front of business card will have logo, name, address, & telephone number. Back of card will have a list of services provided - Roads, Substation Pads, Temporary Pads, Site Pads, Land Leveling, Powerline Row Cleaning, Land Clearing, Gates, Fencing, Construction Entrances, Excavation, Trenching, Underground Utilities, Directional Boring, Pile Driving. We are a construction company that uses heavy equipment like bulldozers, motor graders/blades, dump trucks, backhoes, hydro axes, & skid loaders. We build roads, pads, & install electric utility lines & waterlines underground. This logo is new. The word "Construction" can be smaller as uploaded 2 example edited logos. We will be using this card design for many employees.
Target Market(s)
Industrial Electric Powerline, Wind Turbine, Solar Panel, & Water Utility companies.
Contact Information for Business Card
Name/Position - Dorian Quale - Owner
Address: 4837 FM 582
Merkel, TX 79418
Phone number - (325) 418-2906

```html
<!DOCTYPE html>
<html lang="en">
<head>
<meta charset="utf-8">
<title>Marrow Business Cards</title>
<link href="https://fonts.googleapis.com/css2?family=Montserrat:wght@400;600;700&display=swap" rel="stylesheet">
<style>
  :root {
    --page: #e6e6e6;
    --card-white: #ffffff;
    --ink: #1c1c1c;
    --charcoal: #2f2f2f;
    --graphite: #474747;
    --slate: #5e5e5e;
    --mist: #d9d9d9;
    --paper-text: #f4f4f4;
  }
  * { box-sizing: border-box; margin: 0; padding: 0; }
  html, body { width: 1200px; height: 800px; overflow: hidden; }
  body {
    background: var(--page);
    font-family: "Montserrat", Arial, sans-serif;
    display: flex;
    align-items: center;
    justify-content: center;
    gap: 40px;
  }
  .card {
    position: relative;
    width: 540px;
    height: 309px;
    overflow: hidden;
    box-shadow: 0 10px 26px rgba(0,0,0,0.25);
  }
  .card-art { position: absolute; inset: 0; width: 100%; height: 100%; }

  /* Back: services */
  .card-back { background: var(--card-white); color: var(--ink); }
  .services-title {
    position: absolute; left: 32px; top: 34px;
    font-weight: 700; font-size: 21px; letter-spacing: 0.3px;
    white-space: nowrap;
    padding-bottom: 4px; border-bottom: 2px solid var(--ink);
  }
  .services-list {
    position: absolute; top: 78px;
    list-style: none; font-weight: 600; font-size: 12px; line-height: 19px;
    text-transform: uppercase; white-space: nowrap;
  }
  .services-list li::before { content: "\2022"; margin-right: 8px; }
  .services-list.col-a { left: 34px; }
  .services-list.col-b { left: 306px; top: 26px; }
  .back-brand {
    position: absolute; left: 28px; bottom: 22px;
    display: flex; align-items: center; gap: 8px;
    color: var(--paper-text); font-weight: 600; font-size: 14px;
    letter-spacing: 1px; text-transform: uppercase;
  }
  .brand-dot { width: 12px; height: 12px; border-radius: 50%; background: var(--paper-text); flex: none; }

  /* Front: contact */
  .card-front { background: var(--charcoal); color: var(--paper-text); }
  .front-identity {
    position: absolute; left: 0; right: 0; top: 58px;
    display: flex; flex-direction: column; align-items: center;
  }
  .front-brand {
    display: flex; align-items: center; gap: 10px;
    font-weight: 600; font-size: 26px; letter-spacing: 2px; text-transform: uppercase;
    white-space: nowrap;
  }
  .front-brand .brand-dot { width: 18px; height: 18px; }
  .brand-rule { width: 200px; height: 1.5px; background: var(--paper-text); margin: 14px 0 10px; }
  .person-name { font-weight: 700; font-size: 17px; letter-spacing: 0.5px; text-transform: uppercase; }
  .person-role { font-weight: 600; font-size: 12px; margin-top: 2px; }
  .contact {
    position: absolute; bottom: 22px;
    display: flex; align-items: center; gap: 7px;
    font-weight: 400; font-size: 13px; white-space: nowrap;
  }
  .contact svg { width: 15px; height: 15px; }
  .contact-phone { left: 24px; }
  .contact-address { right: 24px; }
</style>
</head>
<body>

  <section class="card card-back" aria-label="Card back: services provided">
    <svg class="card-art" viewBox="0 0 540 309" preserveAspectRatio="none" aria-hidden="true">
      <path d="M0 250 C150 235 300 200 540 120 L540 309 L0 309 Z" fill="#ececec"/>
      <path d="M0 262 C170 250 330 215 540 150 L540 309 L0 309 Z" fill="#9a9a9a"/>
      <path d="M0 272 C180 262 340 235 540 185 L540 309 L0 309 Z" fill="#474747"/>
    </svg>
    <h2 class="services-title">SERVICES PROVIDED</h2>
    <ul class="services-list col-a">
      <li>Roads</li>
      <li>Substation Pads</li>
      <li>Temporary Pads</li>
      <li>Site Pads</li>
      <li>Land Leveling,</li>
      <li>Powerline Row Cleaning</li>
      <li>Land Clearing, Gates,</li>
    </ul>
    <ul class="services-list col-b">
      <li>Fencing,</li>
      <li>Construction Entrances</li>
      <li>Excavation,</li>
      <li>Trenching,</li>
      <li>Underground Utilities</li>
      <li>Directional Boring</li>
      <li>Pile Driving</li>
    </ul>
    <div class="back-brand"><span class="brand-dot"></span>Marrow Construction</div>
  </section>

  <section class="card card-front" aria-label="Card front: contact details">
    <svg class="card-art" viewBox="0 0 540 309" preserveAspectRatio="none" aria-hidden="true">
      <path d="M0 0 L0 309 L90 309 C120 200 170 90 270 40 C200 30 100 10 0 0 Z" fill="#3c3c3c"/>
      <path d="M540 0 L540 309 L450 309 C420 200 370 90 270 40 C340 30 440 10 540 0 Z" fill="#3c3c3c"/>
      <path d="M0 309 C140 240 400 240 540 309 Z" fill="#3a3a3a"/>
      <path d="M110 309 C160 150 380 150 430 309 Z" fill="#353535"/>
    </svg>
    <div class="front-identity">
      <div class="front-brand"><span class="brand-dot"></span>Marrow Construction</div>
      <div class="brand-rule"></div>
      <div class="person-name">Dorian Quale</div>
      <div class="person-role">Owner</div>
    </div>
    <div class="contact contact-phone">
      <svg viewBox="0 0 24 24" fill="none" stroke="currentColor" stroke-width="2" aria-hidden="true">
        <path d="M5 3h4l2 5-3 2a12 12 0 0 0 6 6l2-3 5 2v4a2 2 0 0 1-2 2A17 17 0 0 1 3 5a2 2 0 0 1 2-2z"/>
      </svg>
      <span>(325) 418-2906</span>
    </div>
    <div class="contact contact-address">
      <svg viewBox="0 0 24 24" fill="none" stroke="currentColor" stroke-width="2" aria-hidden="true">
        <path d="M12 22s7-7 7-12a7 7 0 0 0-14 0c0 5 7 12 7 12z"/><circle cx="12" cy="10" r="2.5"/>
      </svg>
      <span>4837 FM 582 Merkel, TX 79418</span>
    </div>
  </section>

</body>
</html>
```